VELMOTIK Amazing Business Cards Challenge

Velmoti is a new technology company that will provide engineering and manufacturing services in the electric vehicle industry.

We are looking at a new business card that will support our orientation in providing advanced, innovative solutions. The business card will be lean and present the only information required to be more efficient.

Target Market(s)

Fleet operators, private commercial vehicle operators, delivery companies.

Industry/Entity Type

Business

Contact Information for Business Card

Use the logo and its colors, use a white background.

Font styles to use
Sans Serif

Colors
0455a3
ffffff
9bcb3c

Requirements
Must have
• Velmotik Logo
• All informations in the DOC file = 3 different cards.
• White background
Nice to have
• Icons for email, phone and web address.
• Cute design and strong identity.
Should not have
• Bleeds

```html
<!DOCTYPE html>
<html lang="fr">
<head>
<meta charset="utf-8">
<title>Velmotik – Cartes d'affaires</title>
<link rel="stylesheet" href="https://fonts.googleapis.com/css2?family=Open+Sans:wght@300;400;600;700&display=swap">
<style>
  :root {
    --brand-blue: #0455a3;
    --brand-green: #9bcb3c;
    --card-white: #ffffff;
    --backdrop: #ececec;
    --ink-dark: #222326;
    --ink-grey: #6f7073;
    --wordmark-grey: #58595b;
    --card-edge: #dcdcdc;
  }
  * { box-sizing: border-box; margin: 0; padding: 0; }
  html, body {
    width: 1200px; height: 800px; overflow: hidden;
    background: var(--backdrop);
    font-family: "Open Sans", Arial, sans-serif;
  }
  .canvas { position: relative; width: 1200px; height: 800px; }

  .card {
    position: absolute;
    width: 520px; height: 300px;
    background: var(--card-white);
    border: 1px solid var(--card-edge);
    box-shadow: 0 2px 6px rgba(0,0,0,0.08);
  }
  .card--vp { left: 300px; top: 70px; }
  .card--ceo { left: 560px; top: 410px; }

  .card__brand {
    position: absolute; right: 34px; top: 34px;
    display: flex; align-items: center; gap: 8px;
  }
  .brand-square { width: 18px; height: 18px; background: var(--brand-blue); }
  .brand-name {
    font-size: 22px; font-weight: 400; letter-spacing: 0.5px;
    color: var(--wordmark-grey); line-height: 1;
  }

  .card__rule {
    position: absolute; left: 28px; right: 34px; top: 150px;
    height: 1.5px; background: var(--brand-green);
  }
  .card__name {
    position: absolute; left: 28px; top: 112px;
    font-size: 25px; font-weight: 600; color: var(--ink-dark); white-space: nowrap;
  }
  .card__name .credentials { font-weight: 300; }
  .card__title {
    position: absolute; left: 28px; top: 158px;
    font-size: 11.5px; color: var(--brand-green); white-space: nowrap;
  }
  .card__contacts {
    position: absolute; left: 28px; top: 180px;
    list-style: none; font-size: 11px; color: var(--ink-grey); line-height: 15px;
  }
  .card__contacts li { display: flex; align-items: center; gap: 8px; white-space: nowrap; }
  .card__contacts .phone { font-weight: 700; color: var(--ink-dark); }
  .contact-icon { width: 10px; height: 10px; fill: var(--brand-green); flex: none; }

  .brand-lockup {
    position: absolute; left: 44px; top: 610px;
    display: flex; align-items: center; gap: 18px;
  }
  .brand-lockup .brand-square { width: 48px; height: 48px; }
  .brand-lockup .brand-name { font-size: 64px; letter-spacing: 2px; }
</style>
</head>
<body>
<svg width="0" height="0" style="position:absolute" aria-hidden="true">
  <symbol id="icon-phone" viewBox="0 0 10 10"><path d="M2 0.5 L3.6 2.6 L2.8 3.6 Q3.6 5.6 6.2 7.2 L7.2 6.3 L9.5 7.8 L8.4 9.5 Q4.6 9.4 0.5 4.4 Q0.4 1.8 2 0.5Z"/></symbol>
  <symbol id="icon-mail" viewBox="0 0 10 10"><path d="M0.5 2 H9.5 V8 H0.5Z M1.2 2.6 L5 5.6 L8.8 2.6" fill="none" stroke="#9bcb3c" stroke-width="1"/></symbol>
  <symbol id="icon-web" viewBox="0 0 10 10"><g fill="none" stroke="#9bcb3c" stroke-width="0.9"><circle cx="5" cy="5" r="4.3"/><ellipse cx="5" cy="5" rx="1.8" ry="4.3"/><path d="M0.7 5 H9.3"/></g></symbol>
  <symbol id="icon-pin" viewBox="0 0 10 10"><path d="M5 9.6 Q1.6 5.6 1.6 3.6 A3.4 3.4 0 0 1 8.4 3.6 Q8.4 5.6 5 9.6Z M5 2.3 A1.2 1.2 0 1 0 5 4.7 A1.2 1.2 0 1 0 5 2.3Z" fill-rule="evenodd"/></symbol>
</svg>

<main class="canvas">
  <article class="card card--vp">
    <div class="card__brand"><span class="brand-square"></span><span class="brand-name">velmotik</span></div>
    <h2 class="card__name">Étienne Lavallée</h2>
    <div class="card__rule"></div>
    <p class="card__title">V.P. Développement des affaires | V.P. Business Development</p>
    <ul class="card__contacts">
      <li class="phone"><svg class="contact-icon"><use href="#icon-phone"/></svg>+1.555.018.0274</li>
      <li><svg class="contact-icon"><use href="#icon-mail"/></svg>elavallee@velmotik.com</li>
      <li><svg class="contact-icon"><use href="#icon-web"/></svg>velmotik.com</li>
      <li><svg class="contact-icon"><use href="#icon-pin"/></svg>412 – 150 Rue des Érables, Laval (Québec) H7N 2K4 Canada</li>
    </ul>
  </article>

  <article class="card card--ceo">
    <div class="card__brand"><span class="brand-square"></span><span class="brand-name">velmotik</span></div>
    <h2 class="card__name">Mathieu Bellerose<span class="credentials">, ing., M.Sc.A.</span></h2>
    <div class="card__rule"></div>
    <p class="card__title">Président | CEO</p>
    <ul class="card__contacts">
      <li class="phone"><svg class="contact-icon"><use href="#icon-phone"/></svg>+1.555.018.0274</li>
      <li><svg class="contact-icon"><use href="#icon-mail"/></svg>mbellerose@velmotik.com</li>
      <li><svg class="contact-icon"><use href="#icon-web"/></svg>velmotik.com</li>
      <li><svg class="contact-icon"><use href="#icon-pin"/></svg>412 – 150 Rue des Érables, Laval (Québec) H7N 2K4 Canada</li>
    </ul>
  </article>

  <div class="brand-lockup"><span class="brand-square"></span><span class="brand-name">velmotik</span></div>
</main>
</body>
</html>
```